Business logo needed for cards, flyers and a banner

I need a design for my new nappy cake business. I make nappy cakes out of diposible nappies and other baby items. The nappy cakes can be personlised and can make them for baby boys, baby girls or make them gender nuetral.
Updates

I need a design for business cards to start off, but then would like to use the logo from the cards for my business logo. 

Industry/Entity Type

Baby

Contact Information for Business Card

Lorna's Baby Cakes
Lorna Pettigrew
0418462713
lkpettigrew@fernmail.com.au

Requirements
Nice to have
• Maybe a picture of a baby and a nappy cake in the design

```html
<!DOCTYPE html>
<html lang="en">
<head>
<meta charset="utf-8">
<title>Lorna's Baby Cakes – Business Card</title>
<link rel="stylesheet" href="https://fonts.googleapis.com/css2?family=Questrial&display=swap">
<style>
  :root {
    --backdrop: #d8d2cc;
    --card-white: #ffffff;
    --band-brown: #8c7369;
    --mark-brown: #8c7369;
    --name-pink: #de5670;
    --text-light: #ffffff;
    --shadow: rgba(60, 45, 38, 0.18);
  }
  * { margin: 0; padding: 0; box-sizing: border-box; }
  html, body {
    width: 1200px;
    height: 800px;
    overflow: hidden;
    background: var(--backdrop);
  }
  .canvas {
    width: 1200px;
    height: 800px;
    display: flex;
    align-items: center;
    justify-content: center;
  }
  .business-card {
    width: 900px;
    height: 540px;
    background: var(--card-white);
    box-shadow: 0 10px 30px var(--shadow);
    display: flex;
    flex-direction: column;
    font-family: "Questrial", "Century Gothic", sans-serif;
  }
  .brand-area {
    flex: 0 0 330px;
    display: flex;
    align-items: center;
    justify-content: center;
    gap: 34px;
    padding-top: 10px;
  }
  .brand-dot {
    width: 160px;
    height: 160px;
    border-radius: 50%;
    background: var(--mark-brown);
    flex: none;
  }
  .brand-name {
    color: var(--name-pink);
    font-size: 62px;
    font-weight: 400;
    letter-spacing: 1px;
    line-height: 1;
  }
  .contact-band {
    flex: 1;
    background: var(--band-brown);
    color: var(--text-light);
    padding: 40px 70px 0 70px;
    font-size: 30px;
    font-weight: 400;
    line-height: 1.55;
  }
  .contact-row {
    display: flex;
    gap: 36px;
  }
  .contact-name { padding-left: 226px; }
</style>
</head>
<body>
  <main class="canvas">
    <article class="business-card">
      <header class="brand-area">
        <div class="brand-dot" aria-hidden="true"></div>
        <h1 class="brand-name">Lorna's Baby Cakes</h1>
      </header>
      <section class="contact-band">
        <p class="contact-name">Lorna Pettigrew</p>
        <p class="contact-row">
          <span class="contact-phone">0418 462 713</span>
          <span class="contact-email">lkpettigrew@fernmail.com.au</span>
        </p>
      </section>
    </article>
  </main>
</body>
</html>
```